Diaper Crisis Infographic

We are a homeless shelter. Among other things we provide diapers, formula, and other basic necessities for homeless families. We give out over 5,500 diapers each month! We are holding a diaper drive in the month of August to help bolster our supply of diapers. This infographic will be to share via social media to help people to see the incredible need and inspire them to donate diapers or hold diaper drives themselves.

It just so happens that the Review of Child Medicine just released a study that has some pertinent information regarding the "Diaper Crisis" among low income families in America.

Here is the key data from the study:

1 in 3 mothers cut back on essentials (food, child care, utilities) to afford diapers
A single mother working full time at min wage would use 6% of gross income on diapers, that's $18 a week for diapers on avg ($936 a year)
8%(1 in 12) of women interviewed had stretched a diaper by leaving a wet one on longer or partially cleaning and reusing it.
30% of mothers had experienced a time when they could not afford to buy the diapers their kids needed.
10% turned to family or friends
10% turned to an agency or diaper bank
3% turned to other sources like a church
Worry about how to pay for diapers in among top stressors for low income parents, next to food and housing.
Our Ellwood program gives out 5500 diapers a month

A summary article of the study can be found here http://www.trovenews.example/health/it-made-me-feel-ashamed-poor-moms-anguish-over-diaper-6C10775589 and here http://www.harborpost.example/news/science/hp-sci-diaper-need-20130729,0,1515372.story

You can see our color scheme at http://bramblehearth.org/ Not looking for an exact match on the colors or design, but something that flows well would be nice. http://www.bramblehearth.org/diapers has the video that goes along with the diaper drive.

Target Market(s)

Individuals, age 30+

Industry/Entity Type

Church

Requirements
Must have
• Images of babies and or diapers as the graphics. Must include the Kettle & Quilt logo but doesn't need to be prominently displayed. Logo can be green, black, or white.

```html
<!DOCTYPE html>
<html lang="en">
<head>
<meta charset="utf-8">
<title>Diaper Crisis Infographic</title>
<link href="https://fonts.googleapis.com/css2?family=Anton&family=Open+Sans:wght@400;600;700&family=Courier+Prime:wght@700&display=swap" rel="stylesheet">
<style>
  :root {
    --green-deep: #1d6a2c;
    --green-mid: #2f8f3e;
    --green-light: #4aaa4f;
    --lime: #b5cf2f;
    --ink: #2c3a22;
    --white: #ffffff;
    --blue: #2ea6dc;
    --grey: #c8c8c8;
    --orange: #f39a1f;
    --orange-light: #f7ab3a;
    --red: #d7282e;
    --skin-light: #f2dccb;
    --skin-mid: #d9ae93;
  }
  * { box-sizing: border-box; margin: 0; padding: 0; }
  html, body { width: 1200px; height: 3133px; overflow: hidden; }
  body {
    position: relative;
    font-family: "Open Sans", Arial, sans-serif;
    background: radial-gradient(ellipse 80% 55% at 50% 45%, var(--green-light) 0%, var(--green-mid) 45%, var(--green-deep) 100%);
    color: var(--white);
  }
  .abs { position: absolute; }

  .scale-illustration {
    left: 80px; top: 20px; width: 1040px; height: 400px;
    background: radial-gradient(ellipse 60% 60% at 50% 50%, rgba(255,255,255,.35) 0%, rgba(255,255,255,.12) 60%, rgba(255,255,255,0) 100%);
  }

  .headline-frame {
    left: 298px; top: 622px; width: 540px; height: 418px;
    border: 8px solid var(--white);
  }
  .headline-box {
    left: 313px; top: 605px; width: 537px; height: 420px;
    background: var(--lime);
  }
  .headline-ratio {
    left: 313px; top: 612px; width: 537px; text-align: center;
    font-family: "Anton", Impact, sans-serif; color: var(--white);
    font-size: 150px; line-height: 1;
  }
  .headline-ratio .in { font-size: 86px; }
  .headline-noun {
    left: 313px; top: 800px; width: 537px; text-align: center;
    font-family: "Anton", Impact, sans-serif; font-size: 82px; line-height: 1;
  }
  .headline-sub {
    left: 313px; top: 905px; width: 537px; text-align: center;
    font-size: 36px; line-height: 1.2; color: var(--ink);
  }

  .mother-art {
    left: 20px; top: 1120px; width: 110px; height: 165px;
    background: linear-gradient(180deg, rgba(255,255,255,.9), rgba(255,255,255,.7));
  }
  .income-band {
    left: 141px; top: 1112px; width: 993px; height: 188px;
    background: var(--lime); color: var(--ink);
    text-align: center; padding-top: 16px;
  }
  .income-band p { font-size: 27px; line-height: 1.4; }
  .income-band .pct { color: var(--white); font-weight: 700; font-size: 44px; }
  .income-band .money {
    font-family: "Courier Prime", "Courier New", monospace; font-weight: 700;
    color: var(--white); font-size: 38px;
  }

  .stat {
    top: 1363px; width: 220px; color: var(--white);
    padding: 18px 14px; font-size: 22px; line-height: 1.3;
  }
  .stat .num {
    display: block; text-align: center;
    font-weight: 700; font-size: 56px; line-height: 1; margin-bottom: 18px;
  }
  .stat-blue { left: 44px; height: 415px; background: var(--blue); }
  .stat-grey { left: 264px; height: 315px; background: var(--grey); }
  .stat-orange { left: 484px; height: 205px; background: var(--orange); }
  .stat-orange-light { left: 704px; height: 205px; background: var(--orange-light); }
  .stat-red { left: 924px; height: 195px; background: var(--red); }

  .worry-band {
    left: 0; top: 1840px; width: 1200px; height: 200px;
    background: rgba(255,255,255,.18);
  }
  .worry-text {
    left: 0; top: 1858px; width: 1200px; text-align: center;
    font-size: 44px; line-height: 1.25;
  }
  .program-lead {
    left: 0; top: 2060px; width: 1200px; text-align: center;
    font-size: 48px; font-weight: 700;
  }
  .program-count {
    left: 0; top: 2135px; width: 1200px; text-align: center;
    font-family: "Anton", Impact, sans-serif; font-size: 70px; line-height: 1.1;
  }

  .brand { left: 0; top: 2255px; width: 1200px; text-align: center; }
  .brand-mark {
    width: 120px; height: 120px; border-radius: 50%;
    border: 5px solid var(--white); margin: 0 auto 18px;
  }
  .brand-name { font-size: 52px; font-weight: 600; line-height: 1.1; }
  .brand-tag { font-size: 24px; line-height: 1.2; }

  .baby-photo {
    left: 0; top: 2560px; width: 1200px; height: 573px;
    background: linear-gradient(160deg, rgba(242,220,203,0) 0%, var(--skin-light) 30%, var(--skin-mid) 75%, #b88a70 100%);
  }
</style>
</head>
<body>
  <div class="abs scale-illustration" role="img" aria-label="Illustration of a balance scale weighing a diaper against open hands holding a globe of food and essentials"></div>

  <div class="abs headline-frame"></div>
  <div class="abs headline-box"></div>
  <div class="abs headline-ratio">1 <span class="in">in</span> 3</div>
  <div class="abs headline-noun">mothers</div>
  <div class="abs headline-sub">cut back on essentials<br>to afford diapers</div>

  <div class="abs mother-art" role="img" aria-label="Icon of a mother holding a baby"></div>
  <div class="abs income-band">
    <p>A single mother working full time at min wage would use<br>
      <span class="pct">6%</span> of gross income on diapers,<br>
      that's <span class="money">$18 a week</span> for diapers on avg <span class="money">($936 a year)</span></p>
  </div>

  <div class="abs stat stat-blue"><span class="num">8%</span>(1 in 12) of women interviewed had stretched a diaper by leaving a wet one on longer or partially cleaning and reusing it.</div>
  <div class="abs stat stat-grey"><span class="num">30%</span>of mothers had experienced a time when they could not afford to buy the diapers their kids needed.</div>
  <div class="abs stat stat-orange"><span class="num">10%</span>turned to family or friends</div>
  <div class="abs stat stat-orange-light"><span class="num">10%</span>turned to an agency or diaper bank</div>
  <div class="abs stat stat-red"><span class="num">3%</span>turned to other sources like a church</div>

  <div class="abs worry-band"></div>
  <div class="abs worry-text">Worry about how to pay for diapers<br>in among top stressors for low income parents,<br>next to food and housing.</div>

  <div class="abs program-lead">Our Ellwood program gives out</div>
  <div class="abs program-count">5500 diapers a month</div>

  <div class="abs brand">
    <div class="brand-mark"></div>
    <div class="brand-name">Kettle &amp; Quilt</div>
    <div class="brand-tag">Homeless Survival Services<br>Since 1983</div>
  </div>

  <div class="abs baby-photo" role="img" aria-label="Photo of a sleeping newborn baby resting in a parent's hand"></div>
</body>
</html>
```